Business Card Design Project

I want a new business card for all 5 of my companies. Card needs to be double sided with my name and details on one side and all 5 logos on the other side.

Industry/Entity Type

Business

```html
<!DOCTYPE html>
<html lang="en">
<head>
<meta charset="utf-8">
<title>Venturi Group – Business Card</title>
<link rel="stylesheet" href="https://fonts.googleapis.com/css2?family=Arimo:wght@400;700&display=swap">
<style>
  :root {
    --stage: #3a3a3c;
    --card: #ffffff;
    --ink: #5e616b;
    --band: #5f626c;
    --band-text: #f2f3f5;
    --chip: #c3c5ca;
    --dot: #c3c5ca;
    --mascot-name: #1f1f22;
    --figure-a: #f4d27a;
    --figure-b: #4f88c9;
  }
  * { box-sizing: border-box; margin: 0; padding: 0; }
  html, body { width: 1200px; height: 900px; overflow: hidden; }
  body {
    background: var(--stage);
    font-family: "Arimo", Arial, sans-serif;
    color: var(--ink);
    position: relative;
  }
  .card {
    position: absolute;
    top: 308px;
    width: 513px;
    height: 285px;
    background: var(--card);
    overflow: hidden;
  }
  .card--front { left: 73px; }
  .card--back { left: 615px; }

  .group-name {
    position: absolute;
    font-weight: 700;
    font-size: 16px;
    line-height: 16px;
    letter-spacing: -0.3px;
    color: var(--ink);
    white-space: nowrap;
  }
  .card--front .group-name { left: 43px; top: 57px; }
  .name-row {
    position: absolute;
    left: 0; top: 179px;
    display: flex; align-items: baseline;
  }
  .name-chip {
    width: 28px; height: 15px;
    background: var(--chip);
    margin-right: 16px;
    align-self: center;
  }
  .person-name { font-weight: 700; font-size: 19px; color: var(--ink); }
  .person-role { font-size: 15px; margin-left: 9px; color: var(--ink); }
  .contact-band {
    position: absolute;
    left: 0; right: 0; bottom: 0;
    height: 81px;
    background: var(--band);
    color: var(--band-text);
    font-size: 13.5px;
    display: flex;
    padding: 15px 0 0 45px;
  }
  .contact-col { list-style: none; width: 177px; }
  .contact-col li { display: flex; align-items: center; height: 19px; white-space: nowrap; }
  .contact-col svg { width: 10px; height: 10px; margin-right: 5px; fill: var(--band-text); flex: none; }

  .brand {
    position: absolute;
    display: flex; align-items: flex-start;
    font-weight: 700;
    font-size: 16px;
    line-height: 16px;
    letter-spacing: -0.3px;
    color: var(--ink);
    white-space: nowrap;
  }
  .brand-dot { width: 11px; height: 11px; border-radius: 50%; margin: 2px 6px 0 0; flex: none; background: var(--dot); }
  .brand--structural { left: 40px; top: 60px; }
  .brand--sealing { left: 183px; top: 60px; }
  .card--back .group-name { left: 383px; top: 60px; }

  .mascot {
    position: absolute;
    top: 132px;
    width: 150px;
    text-align: center;
  }
  .mascot-figure {
    width: 104px; height: 104px;
    margin: 0 auto;
    border-radius: 8px;
    background: linear-gradient(180deg, var(--figure-a) 0%, var(--figure-b) 100%);
  }
  .mascot-name { font-weight: 700; font-size: 19px; color: var(--mascot-name); margin-top: 6px; white-space: nowrap; }
  .mascot--rig { left: 7px; }
  .mascot--barrier { left: 177px; }
  .mascot--render { left: 345px; }
</style>
</head>
<body>
  <section class="card card--front">
    <div class="group-name">Venturi Group<br>of Companies</div>
    <div class="name-row">
      <span class="name-chip"></span>
      <span class="person-name">Marco Venturi</span>
      <span class="person-role">founder &amp; owner</span>
    </div>
    <div class="contact-band">
      <ul class="contact-col">
        <li><svg viewBox="0 0 10 10"><rect x="2.5" y="0" width="5" height="10" rx="1"/></svg>04 5550 1234</li>
        <li><svg viewBox="0 0 10 10"><path d="M0 3h10v6H0zM2 1h6v2H2z"/></svg>08 5550 2077</li>
      </ul>
      <ul class="contact-col">
        <li><svg viewBox="0 0 10 10"><path d="M0 2h10v6H0z"/></svg>info@venturigroup.com.au</li>
        <li><svg viewBox="0 0 10 10"><circle cx="5" cy="5" r="5"/></svg>www.venturigroup.com.au</li>
      </ul>
    </div>
  </section>

  <section class="card card--back">
    <div class="brand brand--structural"><span class="brand-dot"></span><span>Venturi<br>Structural</span></div>
    <div class="brand brand--sealing"><span class="brand-dot"></span><span>Sitewide<br>Sealing Services</span></div>
    <div class="group-name">Venturi Group<br>of Companies</div>

    <div class="mascot mascot--rig">
      <div class="mascot-figure" role="img" aria-label="Mascot illustration: builder in hard hat holding a spanner beside scaffolding"></div>
      <div class="mascot-name">Mr.Rig</div>
    </div>
    <div class="mascot mascot--barrier">
      <div class="mascot-figure" role="img" aria-label="Mascot illustration: builder in hard hat giving a thumbs up beside a temporary fence panel"></div>
      <div class="mascot-name">Mr.Barrier</div>
    </div>
    <div class="mascot mascot--render">
      <div class="mascot-figure" role="img" aria-label="Mascot illustration: builder in hard hat holding a trowel and plaster hawk"></div>
      <div class="mascot-name">Mr.Render</div>
    </div>
  </section>
</body>
</html>
```